Ledger Ready Business Card

I need a business card designed around my logo (which was designed here on Sketch Yard!)

Target Market(s)

Professional Businesses

Industry/Entity Type

Business

Requirements
Must have
• Details that must be on the business card:

Harriet Vantos
Director
0491 263 358
harriet@ledgerready.com.au
www.ledgerready.com.au
PO Box 4471 Fitzroy North Vic 3068

```html
<!DOCTYPE html>
<html lang="en">
<head>
<meta charset="utf-8">
<title>Ledger Ready Business Card</title>
<link rel="stylesheet" href="https://fonts.googleapis.com/css2?family=Open+Sans:wght@400;600;700&display=swap">
<style>
  :root {
    --red: #c8161d;
    --red-deep: #a80f15;
    --red-soft: #d8272b;
    --ink: #1d1d1f;
    --paper: #ffffff;
    --stage: #e9e9eb;
    --card-w: 660px;
    --card-h: 384px;
  }
  * { margin: 0; padding: 0; box-sizing: border-box; }
  html, body {
    width: 1200px; height: 900px; overflow: hidden;
    background: var(--stage);
    font-family: "Open Sans", Arial, sans-serif;
  }
  .stage {
    width: 1200px; height: 900px;
    display: flex; flex-direction: column; align-items: center; justify-content: center;
    gap: 40px;
  }
  .card {
    position: relative;
    width: var(--card-w); height: var(--card-h);
    overflow: hidden;
    box-shadow: 0 6px 18px rgba(0,0,0,0.18);
  }
  .card-shapes { position: absolute; inset: 0; }

  /* Back */
  .card--back {
    background: linear-gradient(135deg, var(--red-soft), var(--red-deep));
    display: flex; align-items: center; justify-content: center;
  }
  .brand { display: flex; align-items: center; gap: 14px; }
  .brand-dot { width: 40px; height: 40px; border-radius: 50%; }
  .brand-name {
    font-weight: 600; letter-spacing: 2px; text-transform: uppercase;
    white-space: nowrap;
  }
  .card--back .brand-dot { background: var(--paper); }
  .card--back .brand-name { color: var(--paper); font-size: 38px; }

  /* Front */
  .card--front { background: var(--paper); }
  .card--front .brand { position: absolute; left: 44px; top: 52px; }
  .card--front .brand-dot { background: var(--red); width: 44px; height: 44px; }
  .card--front .brand-name { color: var(--ink); font-size: 32px; }

  .contact { position: absolute; left: 186px; top: 146px; }
  .contact-name { color: var(--red); font-size: 20px; font-weight: 400; line-height: 1.3; }
  .contact-role { color: var(--ink); font-size: 15px; font-weight: 700; margin-bottom: 14px; }
  .contact-list { display: grid; grid-template-columns: auto auto; column-gap: 10px; row-gap: 2px; }
  .contact-label { color: var(--red); font-size: 16px; text-align: right; white-space: nowrap; }
  .contact-value { color: var(--ink); font-size: 16px; white-space: nowrap; }

  .address {
    position: absolute; right: 40px; bottom: 15px;
    color: var(--paper); font-size: 17px; opacity: 0.92;
    white-space: nowrap;
  }
</style>
</head>
<body>
<main class="stage">

  <section class="card card--back" aria-label="Business card back">
    <div class="brand">
      <span class="brand-dot"></span>
      <span class="brand-name">Ledger Ready</span>
    </div>
  </section>

  <section class="card card--front" aria-label="Business card front">
    <svg class="card-shapes" viewBox="0 0 660 384" width="660" height="384" aria-hidden="true">
      <polygon points="510,180 660,180 660,330 510,330" fill="var(--red)"/>
      <polygon points="560,118 596,118 660,140 660,164 632,164" fill="var(--red)"/>
      <polygon points="590,96 618,96 660,108 660,126" fill="var(--red)"/>
      <rect x="0" y="330" width="660" height="54" fill="var(--red-deep)"/>
    </svg>

    <div class="brand">
      <span class="brand-dot"></span>
      <span class="brand-name">Ledger Ready</span>
    </div>

    <div class="contact">
      <p class="contact-name">Harriet Vantos</p>
      <p class="contact-role">Director</p>
      <div class="contact-list">
        <span class="contact-label">phone</span><span class="contact-value">0491 263 358</span>
        <span class="contact-label">email</span><span class="contact-value">harriet@ledgerready.com.au</span>
        <span class="contact-label">web</span><span class="contact-value">www.ledgerready.com.au</span>
      </div>
    </div>

    <p class="address">PO Box 4471 Fitzroy North Vic 3068</p>
  </section>

</main>
</body>
</html>
```